Velvet Harbor for sale at the 2019 Tandor Crest Mare Auction on 30 May 2019

I am selling my broodmare at the 2019 Tandor Crest Mare auction on 30 May 2019. I need a flyer to hand out to potential buyers. I have included the required information in the attached word document. I can provide more images if required. I am thinking that a DL double sided or an A5 will suit best. I'm happy to provide more information as required.

Target Market(s)

Race horse breeders, people who buy broodmares.

Font styles to use
Serif
Sans Serif
Script

Colors

Designer to choose colors to be used in the design.

Requirements
Must have
• All of the content provided in the attached brief, however it is not necessary to have the words exactly as per the brief. The brief is for information purposes.
Nice to have
• Innovation...

```html
<!DOCTYPE html>
<html lang="en">
<head>
<meta charset="utf-8">
<title>Velvet Harbor – Tandor Crest Mare Auction Flyer</title>
<link rel="stylesheet" href="https://fonts.googleapis.com/css2?family=Hind:wght@500;600;700&family=Saira+Semi+Condensed:wght@600;700&display=swap">
<style>
  :root {
    --backdrop: #dfe3e2;
    --ink-dark: #333232;
    --band-dark: rgba(44, 43, 46, 0.92);
    --signal-yellow: #f7e41a;
    --signal-red: #e8222b;
    --paper: #f6ecea;
    --white: #ffffff;
    --photo-front: #a9aa8c;
    --photo-back: #8d926f;
  }
  * { box-sizing: border-box; margin: 0; padding: 0; }
  html, body { width: 1200px; height: 800px; overflow: hidden; }
  body {
    background: var(--backdrop);
    font-family: "Hind", "Helvetica Neue", Arial, sans-serif;
    position: relative;
  }
  .page {
    position: absolute;
    top: 46px;
    width: 500px;
    height: 708px;
    overflow: hidden;
    background: var(--paper);
    box-shadow: 0 6px 18px rgba(0,0,0,0.18);
  }
  .page--front { left: 75px; }
  .page--back { left: 625px; }

  .photo { position: absolute; inset: 0; }
  .photo--front { background: var(--photo-front); }
  .photo--back { background: var(--photo-back); }

  /* Front */
  .title-band {
    position: absolute; left: 0; top: 84px;
    width: 392px; height: 56px;
    background: var(--signal-red);
    color: var(--white);
    font-family: "Saira Semi Condensed", "Arial Narrow", sans-serif;
    font-weight: 700; font-size: 38px; letter-spacing: 1px;
    line-height: 56px; padding-left: 36px;
    white-space: nowrap;
  }
  .lot-band {
    position: absolute; left: 0; top: 140px;
    width: 350px; height: 44px;
    background: var(--signal-yellow);
    color: var(--ink-dark);
    font-weight: 700; font-size: 24px; line-height: 48px; padding-left: 36px;
  }
  .sale-date {
    position: absolute; left: 30px; bottom: 96px;
    width: 190px; padding: 14px 20px 10px;
    background: var(--signal-yellow);
    color: var(--ink-dark);
    clip-path: polygon(0 12%, 100% 0, 92% 100%, 4% 96%);
    line-height: 1;
  }
  .sale-date__label { font-size: 26px; font-weight: 500; display: block; }
  .sale-date__day { font-size: 36px; font-weight: 700; display: block; }
  .sale-name {
    position: absolute; right: 22px; bottom: 110px;
    text-align: right; line-height: 1;
  }
  .sale-name span {
    display: inline-block; margin-top: 4px;
    background: var(--signal-yellow); color: var(--ink-dark);
    font-weight: 700; font-size: 24px; padding: 5px 8px 1px;
  }

  /* Back */
  .results { position: absolute; inset: 0; list-style: none; }
  .result {
    position: absolute; left: 0; width: 100%; height: 86px;
  }
  .result__marker {
    position: absolute; left: 16px; top: -6px;
    width: 34px; height: 98px;
    background: var(--signal-yellow);
  }
  .result__bar {
    position: absolute; left: 50px; right: 0; top: 0; height: 86px;
    background: var(--band-dark);
    color: var(--white);
    display: flex; align-items: center;
    padding: 0 18px 0 26px;
    text-transform: uppercase;
  }
  .result__headline {
    width: 160px; font-weight: 700; font-size: 14px; line-height: 1.15; letter-spacing: 0.3px;
  }
  .result__detail {
    flex: 1; font-weight: 600; font-size: 11.5px; line-height: 1.22; padding-left: 20px;
  }
  .result:nth-child(1) { top: 48px; }
  .result:nth-child(2) { top: 178px; }
  .result:nth-child(3) { top: 308px; }
  .result:nth-child(4) { top: 438px; }
  .result:nth-child(5) { top: 568px; }
</style>
</head>
<body>
  <section class="page page--front">
    <div class="photo photo--front" role="img" aria-label="Photograph of a racecourse entrance gate and lawn"></div>
    <h1 class="title-band">VELVET HARBOR</h1>
    <p class="lot-band">LOT NUMBER: 127</p>
    <p class="sale-date"><span class="sale-date__label">SALE DATE</span><span class="sale-date__day">30 MAY</span></p>
    <p class="sale-name">
      <span>TANDOR CREST</span><br>
      <span>NATIONAL</span><br>
      <span>MARE</span><br>
      <span>AUCTION</span>
    </p>
  </section>

  <section class="page page--back">
    <div class="photo photo--back" role="img" aria-label="Photograph of the mare racing past the finishing post"></div>
    <ol class="results">
      <li class="result">
        <span class="result__marker"></span>
        <div class="result__bar">
          <p class="result__headline">Velvet Harbor<br>wins by 3.5L</p>
          <p class="result__detail">Class 6 Handicap – 1400m<br>Riverbend Racing Club<br>(Kestrel Park),<br>21 January 2017</p>
        </div>
      </li>
      <li class="result">
        <span class="result__marker"></span>
        <div class="result__bar">
          <p class="result__headline">Velvet Harbor<br>wins by 2.8L</p>
          <p class="result__detail">No more than one metro win<br>Handicap – 1400m<br>Riverbend Racing Club<br>(Kestrel Park),<br>10 December 2016</p>
        </div>
      </li>
      <li class="result">
        <span class="result__marker"></span>
        <div class="result__bar">
          <p class="result__headline">Velvet Harbor<br>beats Corvane<br>by 1.3L</p>
          <p class="result__detail">Class 6 Plate – 1300m<br>Riverbend Racing Club<br>(Kestrel Park),<br>29 April 2017</p>
        </div>
      </li>
      <li class="result">
        <span class="result__marker"></span>
        <div class="result__bar">
          <p class="result__headline">Velvet Harbor<br>wins by 2.3L</p>
          <p class="result__detail">Class 4 Handicap – 1400m<br>Riverbend Racing Club (Marlow Downs),<br>23 November 2016</p>
        </div>
      </li>
      <li class="result">
        <span class="result__marker"></span>
        <div class="result__bar">
          <p class="result__headline">Velvet Harbor<br>wins on debut<br>at Coral Bay!</p>
          <p class="result__detail">Maiden – 1000m Coral Bay<br>Turf Club,<br>23 October 2015</p>
        </div>
      </li>
    </ol>
  </section>
</body>
</html>
```